Flyer for tutoring

The text should be presented in an engaging way to attract potential customers.
Colorfully designed
Around the edge, various objects related to school and the subjects (see text) should be visible.

```html
<!DOCTYPE html>
<html lang="de">
<head>
<meta charset="utf-8">
<title>Nachhilfe Flyer – Vorder- und Rückseite</title>
<link href="https://fonts.googleapis.com/css2?family=Luckiest+Guy&family=Bitter:wght@400;600;700&display=swap" rel="stylesheet">
<style>
  :root{
    --stage:#adadad;
    --magenta:#d4008c;
    --navy:#22339a;
    --yellow:#ffdf1e;
    --purple:#5a0fd6;
    --orange:#e5561c;
    --plum:#7e1e5e;
    --paper:#f4f2f4;
    --label:#111;
  }
  *{box-sizing:border-box;margin:0;padding:0}
  html,body{width:1200px;height:493px;overflow:hidden}
  body{background:var(--stage);font-family:"Bitter",serif;position:relative}
  .flyer{position:absolute;top:28px;width:283px;height:400px;overflow:hidden;background:var(--paper)}
  .flyer--front{left:297px}
  .flyer--back{left:620px}
  .side-label{position:absolute;top:442px;width:283px;text-align:center;font:700 14px/1 Arial,Helvetica,sans-serif;letter-spacing:1px;color:var(--label)}
  .side-label--front{left:297px}
  .side-label--back{left:620px}

  .photo{position:absolute;inset:0}
  .photo--supplies{background:
      radial-gradient(circle at 12% 10%,#c2185b 0 12%,transparent 22%),
      radial-gradient(circle at 88% 8%,#5b2bb5 0 12%,transparent 24%),
      radial-gradient(circle at 6% 62%,#f28c1c 0 8%,transparent 18%),
      radial-gradient(circle at 85% 88%,#2a4cc0 0 16%,transparent 30%),
      radial-gradient(circle at 20% 92%,#3cb0d8 0 12%,transparent 26%),
      radial-gradient(circle at 60% 95%,#f5a1c0 0 10%,transparent 22%),
      #f7f3f8}
  .photo--pencils{top:0;height:94px;bottom:auto;background:
      linear-gradient(180deg,#e9e6e3 0%,#f4f2f4 100%)}

  .lead-box{position:absolute;left:63px;top:30px;width:158px;padding:5px 6px;background:var(--magenta);color:#fff;font:600 9.4px/1.05 "Bitter",serif;text-align:center;transform:rotate(-1deg);box-shadow:1px 2px 3px rgba(0,0,0,.3)}
  .headline{position:absolute;left:0;right:0;top:86px;text-align:center;font:24px/1.12 "Luckiest Guy",cursive;color:var(--navy);letter-spacing:.3px}
  .tag{position:absolute;left:135px;top:172px;width:111px;padding:5px 4px;background:var(--yellow);color:var(--navy);font:7.4px/1.15 "Luckiest Guy",cursive;text-align:center;transform:rotate(3deg);box-shadow:1px 2px 3px rgba(0,0,0,.3)}
  .intro{position:absolute;left:55px;top:207px;width:126px;font:6.6px/1.05 "Bitter",serif;color:var(--plum)}
  .call-badge{position:absolute;left:166px;top:275px;width:82px;height:82px;border-radius:50%;background:var(--magenta);color:#fff;text-align:center;font-family:"Luckiest Guy",cursive;transform:rotate(8deg);padding-top:15px;box-shadow:1px 2px 4px rgba(0,0,0,.3)}
  .call-badge__cta{font-size:7px;line-height:1.1}
  .call-badge__num{font-size:14px;line-height:1;margin-top:3px}

  .pencil-row{position:absolute;left:0;top:0}
  .lesson-text{position:absolute;left:38px;width:208px;top:93px;text-align:center;font:600 7.6px/1.02 "Bitter",serif;color:var(--orange)}
  .next-text{position:absolute;left:38px;width:208px;top:158px;text-align:center;font:6.8px/1.05 "Bitter",serif;color:var(--plum)}
  .motivation{position:absolute;left:40px;top:183px;width:219px;padding:7px 4px;background:var(--yellow);color:var(--navy);font:10px/1.15 "Luckiest Guy",cursive;text-align:center;transform:rotate(2deg);box-shadow:1px 2px 3px rgba(0,0,0,.3)}
  .about-title{position:absolute;left:36px;top:242px;font:700 7.2px/1 "Bitter",serif;color:var(--plum)}
  .about-text{position:absolute;left:36px;top:254px;width:118px;font:6.6px/1.05 "Bitter",serif;color:var(--plum)}
  .greeting-badge{position:absolute;left:166px;top:248px;width:82px;height:82px;border-radius:50%;background:var(--purple);color:#fff;font:700 6.8px/1.15 "Bitter",serif;text-align:center;display:flex;align-items:center;justify-content:center;padding:10px;transform:rotate(8deg)}
  .contact-band{position:absolute;left:11px;top:334px;width:262px;height:80px;background:var(--magenta);color:#fff;transform:rotate(1.5deg);padding:10px 12px 0;text-align:right}
  .contact-band__title{font:700 8.4px/1.1 "Bitter",serif}
  .contact-band__line{font:600 7.8px/1.15 "Bitter",serif}
  .contact-band__phone{font:6.8px/1.2 "Bitter",serif;text-align:left;margin-top:-2px}
</style>
</head>
<body>

<section class="flyer flyer--front" aria-label="Flyer Vorderseite">
  <div class="photo photo--supplies" role="img" aria-label="Foto von Schulsachen rundherum: Stifte, Spitzer, Radiergummi, Schere, Lineal auf Papier"></div>
  <p class="lead-box">Möchtest du dich gerne in der Schule verbessern und suchst eine</p>
  <h1 class="headline">Professionelle<br>Nachhilfelehrerin/<br>Lerncoach</h1>
  <p class="tag">Dann lass es uns<br>doch mal versuchen!</p>
  <p class="intro">Die erste Lektion – die Kennenlernlektion – dauert ca. 30 Minuten. Sie ist kostenlos. Denn wir müssen ja sicher gehen, dass wir uns verstehen und leiden können. Bei unserem ersten Treffen legen wir auch fest, woran wir arbeiten werden und wann die Nachhilfe in deine Agenda passt.</p>
  <div class="call-badge">
    <div class="call-badge__cta">Kontaktieren<br>Sie mich</div>
    <div class="call-badge__num">079 512<br>44 80</div>
  </div>
</section>

<section class="flyer flyer--back" aria-label="Flyer Rückseite">
  <div class="photo photo--pencils" role="img" aria-label="Foto von Farbstiftspitzen, die von oben ins Bild ragen"></div>
  <p class="lesson-text">Die erste Lektion – die Kennenlernlektion – dauert ca. 30 Minuten. Sie ist kostenlos. Denn wir müssen ja sicher gehen, dass wir uns verstehen und leiden können. Bei unserem ersten Treffen legen wir auch fest, woran wir arbeiten werden und wann die Nachhilfe in deine Agenda passt.</p>
  <p class="next-text">Wenn der erste Eindruck stimmt, dann legen wir los, und bald schon werden</p>
  <p class="motivation">Deine Motivation und<br>deine Noten besser und besser!</p>
  <h2 class="about-title">Zu meiner Person:</h2>
  <p class="about-text">Ich wohne hier in der Siedlung am Lindenweg und bin ausgebildete und sehr erfahrene Sekundar- und Primarlehrerin in den Fächern Deutsch, Französisch, Englisch und Geschichte. (Auf Wunsch auch Mathe-Nachhilfe möglich.)</p>
  <p class="greeting-badge">Ich freue mich auf deine Kontaktaufnah me! Bis bald!</p>
  <div class="contact-band">
    <p class="contact-band__title">Meine Kontaktdaten:</p>
    <p class="contact-band__line">Mail: lena.maurer@mailbox.ch</p>
    <p class="contact-band__phone"><b>Tel.</b> 079 512 44 80 (nachmittags fast immer erreichbar)</p>
  </div>
</section>

<p class="side-label side-label--front">FRONT</p>
<p class="side-label side-label--back">BACK</p>

</body>
</html>
```